Fernbrook Pet Showcase Ticket Card Design

We’re looking to create a complimentary “ticket” card for Fernbrook Pet Showcase that can be handed out physically. We host an event for cat lovers. The card should feel special and collectible. Size will be a standard business card (3.5" x 2") Orientation is open to designer recommendation. This ticket will be used as a complimentary entry pass for select guests, partners, & giveaways. Key elements to Include are the Fernbrook Pet Showcase logo (provided), the words “Complimentary Ticket” or similar wording (open to creative phrasing and cat puns) A blank space for the Event date (to be written in) & Ticket number (to be written in) . Event Name is always "Fernbrook Pet Bazaar & Rehoming Day". We want the ticket to feel clean & modern but slightly playful with a cat-inspired touch (think clever, not kitschy). Could include a subtle cat motif or texture (e.g., whisker lines, paw detail, soft patterning) Open to unique layout ideas that still leave clear writing space. Avoid overcrowding of elements. Ticket should also have fine print "This ticket is not redeemable for cash and cannot be combined with any other offers or discounts, can only be used for the date indicated"

Target Market(s)

Women

Industry/Entity Type

pets

Colors
6B429C
8869AF
B7A5CE
E3DAEB
F3F0F8

Requirements
Must have
• Fernbrook Pet Showcase Logo & words around complimentary ticket as well as the fine print
Nice to have
• cat-inspired touch (think clever, not kitschy). Could include a subtle cat motif or texture (e.g., whisker lines, paw detail, soft patterning)
Should not have
• should not look cartoony

```html
<!DOCTYPE html>
<html lang="en">
<head>
<meta charset="utf-8">
<title>Fernbrook Pet Showcase – Purr-fect Pass</title>
<link rel="stylesheet" href="https://fonts.googleapis.com/css2?family=Baloo+2:wght@500;600;700;800&display=swap">
<style>
  :root {
    --plum: #6B429C;
    --violet: #8869AF;
    --lilac: #B7A5CE;
    --mist: #E3DAEB;
    --haze: #F3F0F8;
    --paper: #FFFFFF;
    --ink-soft: #b29ecf;
  }
  * { margin: 0; padding: 0; box-sizing: border-box; }
  html, body {
    width: 1200px;
    height: 843px;
    overflow: hidden;
    background: var(--paper);
    font-family: "Baloo 2", system-ui, sans-serif;
  }
  .stage {
    position: relative;
    width: 1200px;
    height: 843px;
  }
  .ticket {
    position: absolute;
    left: 277px;
    top: 233px;
    width: 733px;
    height: 419px;
    background: var(--paper);
    overflow: hidden;
    color: var(--ink-soft);
  }
  .ticket__pattern {
    position: absolute;
    inset: 0;
    background: radial-gradient(ellipse at 50% 50%, var(--paper) 0%, var(--haze) 70%, #ece6f4 100%);
  }
  .brand {
    position: absolute;
    left: 0;
    right: 0;
    top: 14px;
    text-align: center;
    font-weight: 800;
    font-size: 46px;
    line-height: 44px;
    color: var(--lilac);
    letter-spacing: 0.5px;
  }
  .brand__rule {
    position: absolute;
    top: 136px;
    left: 266px;
    width: 180px;
    height: 1px;
    background: var(--lilac);
  }
  .pass-band {
    position: absolute;
    left: 236px;
    top: 176px;
    width: 262px;
    height: 36px;
    background: linear-gradient(90deg, var(--violet), #9a7fc0 50%, var(--violet));
    color: var(--paper);
    font-weight: 700;
    font-size: 20px;
    line-height: 38px;
    text-align: center;
    letter-spacing: 0.6px;
  }
  .event-name {
    position: absolute;
    left: 0;
    right: 0;
    top: 264px;
    text-align: center;
    font-weight: 700;
    font-size: 29px;
    line-height: 40px;
    color: var(--lilac);
  }
  .field {
    position: absolute;
    top: 324px;
    display: flex;
    align-items: flex-end;
    gap: 6px;
    font-weight: 700;
    font-size: 22px;
    line-height: 28px;
    color: var(--lilac);
  }
  .field__line {
    display: block;
    height: 2px;
    background: var(--lilac);
    margin-bottom: 6px;
  }
  .field--date { left: 118px; }
  .field--date .field__line { width: 96px; }
  .field--number { left: 423px; gap: 12px; }
  .field--number .field__line { width: 108px; }
  .fine-print {
    position: absolute;
    left: 100px;
    right: 80px;
    top: 376px;
    text-align: center;
    font-weight: 600;
    font-size: 9.6px;
    line-height: 13px;
    color: var(--lilac);
  }
</style>
</head>
<body>
<main class="stage">
  <article class="ticket">
    <div class="ticket__pattern" role="img" aria-label="Faint lavender paw-print pattern scattered across the card"></div>

    <h1 class="brand">Fernbrook<br>Pet Showcase</h1>
    <div class="brand__rule"></div>

    <div class="pass-band">PURR-FECT PASS</div>

    <h2 class="event-name">Fernbrook Pet Bazaar &amp; Rehoming Day</h2>

    <div class="field field--date">
      <span class="field__label">DATE</span>
      <span class="field__line"></span>
    </div>
    <div class="field field--number">
      <span class="field__label">N°CARD</span>
      <span class="field__line"></span>
    </div>

    <p class="fine-print">This ticket is not redeemable for cash and cannot be combined with any other offers or discounts, can<br>only be used for the date indicated"</p>
  </article>
</main>
</body>
</html>
```